Real Estate "For Sale" Sign for construction company

We need a sign that we can use to hang on a post and place on the road when we sell a property. The sign will be simple and will need to mainly feature our logo (files attached), as well as the words "For Sale", and then our phone number "(555) 617 3489". The sign will hang on a post that'll look something like the attached picture.

Target Market(s)

Home buyers

Industry/Entity Type

Real Estate

Font styles to use
Serif
Sans Serif

Colors
0054AA
0677BA
7BADD7
CADEEF
E8F1F8
0094D4
00A9DD
6FCCEA
C7EBF8
E9F6FB

Requirements
Must have
• For Sale & our phone number

```html
<!DOCTYPE html>
<html lang="en">
<head>
<meta charset="utf-8">
<title>For Sale Sign – Blue Hollow Properties</title>
<link rel="stylesheet" href="https://fonts.googleapis.com/css2?family=Lexend:wght@500;600&display=swap">
<style>
  :root {
    --navy: #0054AA;
    --brand: #0677BA;
    --frame: #1DA6DE;
    --paper: #FFFFFF;
  }
  html, body {
    margin: 0;
    padding: 0;
    width: 1200px;
    height: 1200px;
    overflow: hidden;
    background: var(--paper);
  }
  .canvas {
    position: relative;
    width: 1200px;
    height: 1200px;
    font-family: "Lexend", sans-serif;
  }
  .hanger {
    position: absolute;
    top: 325px;
    width: 10px;
    height: 40px;
    background: var(--frame);
  }
  .hanger--left { left: 220px; }
  .hanger--right { left: 977px; }
  .sign {
    position: absolute;
    left: 110px;
    top: 362px;
    width: 987px;
    height: 521px;
    box-sizing: border-box;
    border: 12.5px solid var(--frame);
    background: var(--paper);
  }
  .sign__headline {
    position: absolute;
    left: 94px;
    top: 26px;
    margin: 0;
    font-size: 70px;
    font-weight: 600;
    letter-spacing: -1px;
    color: var(--navy);
    line-height: 1;
  }
  .brand-mark {
    position: absolute;
    left: 50%;
    top: 108px;
    width: 150px;
    height: 150px;
    margin-left: -75px;
    border-radius: 50%;
    background: var(--brand);
  }
  .brand-name {
    position: absolute;
    left: 0;
    right: 0;
    top: 272px;
    text-align: center;
    color: var(--brand);
    font-weight: 600;
    line-height: 1;
  }
  .brand-name__main {
    display: block;
    font-size: 70px;
    letter-spacing: -0.5px;
  }
  .brand-name__sub {
    display: block;
    margin-top: 26px;
    font-size: 26px;
    letter-spacing: 22px;
    padding-left: 22px;
  }
  .sign__phone {
    position: absolute;
    right: 94px;
    top: 445px;
    margin: 0;
    font-size: 31px;
    font-weight: 600;
    color: var(--navy);
    letter-spacing: -0.3px;
    line-height: 1;
  }
</style>
</head>
<body>
  <div class="canvas">
    <span class="hanger hanger--left"></span>
    <span class="hanger hanger--right"></span>
    <section class="sign">
      <h1 class="sign__headline">For Sale</h1>
      <span class="brand-mark" aria-hidden="true"></span>
      <div class="brand-name">
        <span class="brand-name__main">Blue Hollow</span>
        <span class="brand-name__sub">PROPERTIES</span>
      </div>
      <p class="sign__phone">phone number (555) 617 3489</p>
    </section>
  </div>
</body>
</html>
```